New Generation Winery needs inspiring label for special bottling

We are a family owned winery in the Rhine Valley in Germany. Check www.brendel-aumann.de . We have a very exciting project going: In 2014 we harvested our best vinyard and split the grapes in half. First half I have treated the way I have done it over the past 40 years. Second half I gave to my daughter who is just entering the winemaking business. She has treated it in a completely different way - her way - the way of the new generation. One of the differentiators; she has squeezed the juices with her bare feet which reduces acidity and bitterness in the wine (less tannins). This is why we want to call the wine "Mondgrüße" (meaning "Moongreets"). Please be careful when writing the "ß" . It is a German letter which replaces the "double s". It is NOT a capital B!! I Have attached a file which gives you the size of the label and another file which shows the current design of the winery labels. If possible it should pick up some elements from the current design (maybe just the colours?) but otherwise you are free. It will go on a dark green bottle, almost black. Apart from the word "Mondgrüße" you need to place the grape "Riesling", the word "trocken" (means dry) and the year of the harvest "2014".

Industry/Entity Type

Brendel

Requirements
Nice to have
• Update 25.3.2015: Have a look at the attached image "Inspiration". Maybe that is a good thought starter, too. Have fun..

```html
<!DOCTYPE html>
<html lang="de">
<head>
<meta charset="utf-8">
<title>Mondgrüße Riesling – Etikett</title>
<link rel="stylesheet" href="https://fonts.googleapis.com/css2?family=Cormorant+Garamond:wght@500&family=Pinyon+Script&display=swap">
<style>
  :root {
    --stage: #646464;
    --frame-red: #a8161f;
    --frame-deep: #7d0f16;
    --frame-orange: #e9781f;
    --paper: #eef0e3;
    --paper-edge: #e3e6d6;
    --ink: #1c1c1c;
    --grey-script: #6f6f72;
    --brand-red: #b3242c;
    --art-light: #f8f8f3;
    --art-shade: #e6e8dc;
    --ornament: #e2e4d6;
    --small-ink: #3a3a3a;
  }
  * { box-sizing: border-box; margin: 0; padding: 0; }
  html, body {
    width: 749px; height: 1200px; overflow: hidden;
    background: var(--stage);
  }
  .label {
    position: absolute; left: 74px; top: 300px;
    width: 600px; height: 600px;
    padding: 18px;
    background: linear-gradient(180deg, var(--frame-deep) 0%, var(--frame-red) 45%, var(--frame-red) 80%, var(--frame-orange) 100%);
    box-shadow: 0 2px 6px rgba(0,0,0,.25);
  }
  .label__paper {
    position: relative; width: 100%; height: 100%;
    background: radial-gradient(ellipse at center, var(--paper) 55%, var(--paper-edge) 100%);
  }
  .ornament {
    position: absolute; width: 130px; height: 80px;
    background: linear-gradient(135deg, var(--ornament), transparent);
    opacity: .7;
  }
  .ornament--tl { left: 12px; top: 12px; }
  .ornament--tr { right: 12px; top: 12px; transform: scaleX(-1); }
  .ornament--bl { left: 12px; bottom: 12px; transform: scaleY(-1); }
  .ornament--br { right: 12px; bottom: 12px; transform: scale(-1,-1); }
  .brand {
    position: absolute; left: 247px; top: 36px; transform: translateX(-50%);
    font: 500 26px "Cormorant Garamond", serif; color: var(--brand-red);
  }
  .footprint-art {
    position: absolute; left: 118px; top: 112px;
    width: 256px; height: 222px;
    background: linear-gradient(160deg, var(--art-light) 0%, var(--art-shade) 100%);
    clip-path: polygon(0 0, 70% 0, 70% 45%, 100% 45%, 100% 100%, 0 100%);
  }
  .wine-name {
    position: absolute; left: 302px; top: 148px;
    font: 500 40px "Cormorant Garamond", serif; color: var(--ink);
  }
  .grape {
    position: absolute; left: 0; right: 0; top: 336px; text-align: center;
    padding-left: 10px;
    font: 400 100px "Pinyon Script", cursive; color: var(--grey-script);
    line-height: 1;
  }
  .style {
    position: absolute; left: 0; right: 0; top: 498px; text-align: center;
    font: 500 20px "Cormorant Garamond", serif; letter-spacing: 1px; color: var(--small-ink);
  }
  .vintage {
    position: absolute; left: 0; right: 0; top: 524px; text-align: center;
    font: 500 13px "Cormorant Garamond", serif; color: var(--small-ink);
  }
</style>
</head>
<body>
  <div class="label">
    <div class="label__paper">
      <div class="ornament ornament--tl" role="img" aria-label="Zierranke oben links"></div>
      <div class="ornament ornament--tr" role="img" aria-label="Zierranke oben rechts"></div>
      <div class="ornament ornament--bl" role="img" aria-label="Zierranke unten links"></div>
      <div class="ornament ornament--br" role="img" aria-label="Zierranke unten rechts"></div>

      <div class="brand">Brendel</div>

      <div class="footprint-art" role="img" aria-label="Illustration: zwei weiße Fußabdrücke"></div>

      <div class="wine-name">Mondgrüße</div>
      <div class="grape">Riesling</div>
      <div class="style">TROCKEN</div>
      <div class="vintage">2014</div>
    </div>
  </div>
</body>
</html>
```